Looking for a Micropage Template

My website will be offering our users to have their very own micropage / profile page hosted on our website.

I am looking for someone to design a a web micropage / profile template that matches the color theme of our websites homepage.

1. Follow the colors of our homepage

2. Open the excel sheet and follow the directions to design a micropage / profile page template.

Target Market(s)

Travel Market

Industry/Entity Type

Travel

Number of Pages Required

1 page

Requirements
Must have
• All of the fields specified in the excel sheet
Nice to have
• Follow the color themes and style of the company homepage
• Different color themes is acceptable as long as it looks nice
• Nice HQ photos

```html
<!DOCTYPE html>
<html lang="en">
<head>
<meta charset="utf-8">
<title>Voyalo Micropage</title>
<link href="https://fonts.googleapis.com/css2?family=Roboto:wght@300;400;500&family=Open+Sans:ital,wght@0,400;0,600;1,400&display=swap" rel="stylesheet">
<style>
  :root {
    --teal: #2aa9b4;
    --teal-bright: #2ecfd0;
    --teal-dark: #2a6d7a;
    --yellow: #f5c530;
    --yellow-light: #fbd84f;
    --yellow-text: #f5d13a;
    --ink: #3a3a3a;
    --muted: #8a8a8a;
    --line: #c9c9c9;
    --footer: #5d5d5f;
    --white: #ffffff;
  }
  * { box-sizing: border-box; margin: 0; padding: 0; }
  html, body { width: 816px; height: 1200px; overflow: hidden; background: var(--white); }
  body { position: relative; font-family: "Roboto", sans-serif; color: var(--ink); }

  .site-header { position: absolute; top: 0; left: 0; width: 816px; height: 58px; background: var(--white); }
  .brand { position: absolute; left: 51px; top: 13px; font: 500 26px "Roboto", sans-serif; color: var(--teal); display: flex; align-items: center; gap: 6px; }
  .brand-dot { width: 10px; height: 10px; border-radius: 50%; background: var(--yellow); }
  .location-picker { position: absolute; right: 46px; top: 23px; font-size: 9.5px; color: var(--ink); display: flex; align-items: center; gap: 5px; }

  .hero { position: absolute; top: 58px; left: 0; width: 816px; height: 349px; }
  .hero-photo { position: absolute; inset: 0; background: linear-gradient(100deg, #2d5fd0 0%, #4a7ee0 40%, #6f97e6 52%, #e8d9bf 62%, #f1e4cb 100%); }
  .profile-card { position: absolute; left: 48px; top: 91px; width: 231px; height: 166px; background: var(--white); border: 3px solid var(--yellow); border-radius: 10px; }
  .avatar { position: absolute; left: 119px; top: 50px; width: 88px; height: 88px; border-radius: 50%; background: linear-gradient(160deg, #d9d3cc, #a4988e); border: 3px solid var(--yellow); }
  .profile-field { position: absolute; left: 13px; width: 201px; height: 28px; border-radius: 14px; background: #efefef; border: 1px solid #d6d6d6; font-size: 9.5px; display: flex; align-items: center; justify-content: center; color: var(--ink); }
  .category-badge { position: absolute; left: 51px; top: 268px; width: 224px; height: 36px; border-radius: 18px; background: var(--teal-bright); border: 3px solid var(--teal-dark); color: var(--white); font-size: 15px; letter-spacing: .3px; display: flex; align-items: center; padding-left: 40px; gap: 22px; }
  .rate-badge { position: absolute; left: 686px; top: 224px; width: 80px; height: 80px; border-radius: 50%; background: var(--yellow); border: 3px solid #d4b24d; text-align: center; color: #1d1d1d; }
  .rate-badge strong { display: block; font: 500 26px "Roboto", sans-serif; margin-top: 15px; line-height: 1; }
  .rate-badge span { font-size: 9.5px; }

  .about { position: absolute; top: 440px; left: 0; width: 816px; }
  .about h1 { position: absolute; left: 50px; top: 4px; font: 500 29px "Roboto", sans-serif; color: var(--teal); letter-spacing: .3px; }
  .about p { position: absolute; left: 51px; top: 50px; width: 472px; font: 300 9.8px/18.7px "Roboto", sans-serif; color: var(--ink); }
  .features { position: absolute; left: 540px; top: 9px; width: 226px; list-style: none; }
  .features li { height: 34px; margin-bottom: 4px; background: linear-gradient(var(--yellow-light), var(--yellow)); border-radius: 2px; color: var(--white); font: 500 10.8px "Roboto", sans-serif; display: flex; align-items: center; justify-content: center; letter-spacing: .3px; }

  .section-divider { position: absolute; top: 628px; left: 0; width: 816px; height: 6px; background: linear-gradient(to bottom, rgba(0,0,0,.06), rgba(0,0,0,0)); }

  .contact h2 { position: absolute; top: 652px; left: 0; width: 816px; text-align: center; font: 600 29px "Open Sans", sans-serif; color: var(--teal); }
  .field { position: absolute; left: 97px; width: 307px; height: 32px; border: 1px solid var(--line); font: 400 9.5px "Open Sans", sans-serif; color: var(--muted); display: flex; align-items: center; justify-content: space-between; padding: 0 13px 0 16px; }
  .message { position: absolute; left: 424px; top: 713px; width: 308px; height: 118px; border: 1px solid var(--line); font: 400 9.5px "Open Sans", sans-serif; color: var(--muted); padding: 9px 11px; }
  .send-button { position: absolute; left: 351px; top: 870px; width: 127px; height: 35px; background: linear-gradient(var(--yellow-light), var(--yellow)); border-radius: 2px; color: var(--white); font: 600 10px "Open Sans", sans-serif; display: flex; align-items: center; justify-content: center; }

  .connect { position: absolute; top: 946px; left: 0; width: 816px; height: 199px; background: var(--teal-bright); }
  .connect-notch { position: absolute; left: 395px; top: -1px; }
  .connect-title { position: absolute; top: 48px; left: 0; width: 816px; text-align: center; font: 400 15px "Open Sans", sans-serif; color: var(--white); }
  .connect-tagline { position: absolute; top: 73px; left: 0; width: 816px; display: block; text-align: center; font: italic 400 13px "Open Sans", sans-serif; color: var(--yellow-text); }
  .social-row { position: absolute; top: 112px; left: 263px; display: flex; gap: 4px; list-style: none; }
  .social-row li { width: 23px; height: 23px; border-radius: 3px; }

  .site-footer { position: absolute; top: 1145px; left: 0; width: 816px; height: 55px; background: var(--footer); color: var(--white); font: 400 8px "Open Sans", sans-serif; }
  .copyright { position: absolute; left: 67px; top: 22px; }
  .legal { position: absolute; right: 66px; top: 23px; }
</style>
</head>
<body>
  <header class="site-header">
    <div class="brand"><span>Voyalo.com</span><span class="brand-dot"></span></div>
    <div class="location-picker">
      <svg width="9" height="9" viewBox="0 0 10 10"><circle cx="5" cy="5" r="4.5" fill="#333"/></svg>
      <span>Country, City</span>
      <svg width="7" height="5" viewBox="0 0 7 5"><path d="M1 1l2.5 2.5L6 1" stroke="#333" fill="none"/></svg>
    </div>
  </header>

  <section class="hero">
    <div class="hero-photo" role="img" aria-label="Photo of a cream apartment building under a blue sky"></div>
    <div class="profile-card">
      <div class="profile-field" style="top:76px">Name</div>
      <div class="profile-field" style="top:118px">Website</div>
    </div>
    <div class="avatar" role="img" aria-label="Profile photo of the host"></div>
    <div class="category-badge">
      <svg width="26" height="24" viewBox="0 0 26 24" aria-hidden="true"><circle cx="9" cy="6" r="4" fill="#fff"/><path d="M2 23c0-7 3-10 7-10s7 3 7 10z" fill="#fff"/><rect x="15" y="6" width="10" height="2" fill="#fff"/></svg>
      <span>RESTAURANT</span>
    </div>
    <div class="rate-badge"><strong>$35</strong><span>Per Hrs</span></div>
  </section>

  <section class="about">
    <h1>HEADING GOES HERE</h1>
    <p>Aliquam molestie, mi et imperdiet euismod, dui purus auctor tellus, et interdum lacus lectus et ante. Sed accumsan sollicitudin sapien, sit amet adipiscing turpis gravida ac. In congue, neque ac lobortis volutpat, libero mauris varius mi, vitae suscipit ipsum ligula vitae risus.&nbsp; Duis aliquam nibh a dui iaculis viverra id a velit. Vivamus egestas risus in magna varius commodo. Sed semper viverra egestas. Etiam pretium porttitor lectus, vel ornare neque porta volutpat.</p>
    <ul class="features">
      <li>SPEAKS MANDARIN</li>
      <li>EXPERIENCED WITH CHINESE TOURISTS</li>
      <li>PROFESSIONALLY LICENSED</li>
      <li>GIVES REFERRAL FEE</li>
    </ul>
  </section>

  <div class="section-divider"></div>

  <section class="contact">
    <h2>CONTACT US</h2>
    <div class="field" style="top:713px"><span>First &amp; Last name</span>
      <svg width="14" height="14" viewBox="0 0 14 14"><circle cx="7" cy="4" r="3.5" fill="#ccc"/><path d="M0 14c0-4 3-6 7-6s7 2 7 6z" fill="#ccc"/></svg></div>
    <div class="field" style="top:757px"><span>Phone No.</span>
      <svg width="14" height="14" viewBox="0 0 14 14"><path d="M3 1l3 3-1.5 2a8 8 0 0 0 3.5 3.5L10 8l3 3-2 2C6 13 1 8 1 3z" fill="#ccc"/></svg></div>
    <div class="field" style="top:800px"><span>Email Id *</span>
      <svg width="14" height="10" viewBox="0 0 14 10"><rect x=".5" y=".5" width="13" height="9" fill="none" stroke="#ccc"/><path d="M.5 .5L7 6l6.5-5.5" fill="none" stroke="#ccc"/></svg></div>
    <div class="message">your message</div>
    <div class="send-button">SEND MESSAGE</div>
  </section>

  <section class="connect">
    <svg class="connect-notch" width="28" height="16" viewBox="0 0 28 16" aria-hidden="true"><path d="M0 0h28L14 15z" fill="#fff"/></svg>
    <h3 class="connect-title">WE WANT TO HEAR FROM YOU</h3>
    <p class="connect-tagline">connect with us</p>
    <ul class="social-row" aria-label="Social network links">
      <li style="background:#3b5998"></li>
      <li style="background:#1da1f2"></li>
      <li style="background:#d34836"></li>
      <li style="background:#0e76a8"></li>
      <li style="background:#cb2027"></li>
      <li style="background:#e6162d"></li>
      <li style="background:#4caf50"></li>
      <li style="background:#ffffff"></li>
      <li style="background:#ffffff"></li>
      <li style="background:#ffffff"></li>
    </ul>
  </section>

  <footer class="site-footer">
    <div class="copyright">©&nbsp;&nbsp;2015 VOYALO.COM . ALL RIGHTS RESERVED</div>
    <div class="legal">TERMS OF SERVICE &nbsp;&nbsp;|&nbsp;&nbsp; PRIVACY POLICY</div>
  </footer>
</body>
</html>
```